KemaTruvi 16 pages booklet CD Cover

I need a cover (also formatted to be used for digital release), a 16 Pages Booklet + Inlay both sides, a back cover, and a CD image for french pop-rock album.

The name of the artist : Kematruvi
The name of the album : Cueillir la brume (which means "picking the mist")
Style of music: I've attached some mp3 extracts. In a few words, this is electro POP music, I'm inspired by band such as The Quill, etc..

This album talks about the desire to live elsewhere, in a world more just and equitable, less painful. The songs talk about people fighting to find a job, to feed their son, poeple who would like to have enough money to enjoy life, etc... but as they can't, at least, they dream about a new world, they draw this elsewhere, hence the title of the album "Cueillir la brume"

Industry/Entity Type

Music Download

Number of Pages Required

5+ page

Font styles to use
Sans Serif

Colors
b768aa
33a6d7

Requirements
Must have
• COver: fell free to make your porposal as long as it match the project description objectoves.
• I have add/attached a document "CD Cover Structure" that explains the stucture of the cover, and how i think it could be setup. BUt any other proposal will be welcome.
• For the last one, we will put the song titles and i will let you make me some suggestions.
Nice to have
• the songs are rather melancholy (but not sad) and it would be nice to transmit this impression by the colors. That's why i have chose the pink and blue as primary colours.

```html
<!DOCTYPE html>
<html lang="fr">
<head>
<meta charset="utf-8">
<title>Kematruvi — Cueillir la brume</title>
<link rel="stylesheet" href="https://fonts.googleapis.com/css2?family=Poppins:wght@300;500&display=swap">
<style>
  :root {
    --paper: #ffffff;
    --frame: #d6d8e2;
    --ink: #26336e;
    --wave-deep: #2a2470;
    --wave-violet: #5a4fb8;
    --wave-lilac: #9d8ee0;
    --wave-glow: #eef1fc;
    --mark-pink: #b768aa;
    --mark-blue: #33a6d7;
  }
  * { margin: 0; padding: 0; box-sizing: border-box; }
  html, body { width: 1200px; height: 1200px; overflow: hidden; background: var(--paper); }

  .album-cover {
    position: relative;
    width: 1200px;
    height: 1200px;
    background: var(--paper);
    font-family: "Poppins", sans-serif;
  }

  .cover-frame {
    position: absolute;
    left: 64px; right: 64px;
    top: 95px; bottom: 95px;
    border: 2px solid var(--frame);
  }

  .soundwave-art {
    position: absolute;
    left: 0; right: 0;
    top: 183px; height: 877px;
    background: linear-gradient(90deg,
      var(--wave-deep) 0%,
      var(--wave-violet) 14%,
      var(--wave-lilac) 30%,
      var(--wave-glow) 50%,
      var(--wave-lilac) 70%,
      var(--wave-violet) 86%,
      var(--wave-deep) 100%);
    -webkit-mask-image: linear-gradient(180deg, transparent 0%, #000 32%, #000 68%, transparent 100%);
            mask-image: linear-gradient(180deg, transparent 0%, #000 32%, #000 68%, transparent 100%);
  }

  .artist-title {
    position: absolute;
    left: 148px; right: 148px;
    top: 612px;
    transform: translateY(-50%);
    display: flex;
    align-items: center;
    gap: 22px;
  }
  .artist-title .rule {
    flex: 1;
    height: 2px;
    background: var(--ink);
  }
  .artist-title h1 {
    font-weight: 300;
    font-size: 60px;
    letter-spacing: 2px;
    color: var(--ink);
    line-height: 1;
  }

  .label-mark {
    position: absolute;
    left: 50%;
    top: 1080px;
    transform: translate(-50%, -50%);
    background: var(--paper);
    padding: 12px 26px;
    display: flex;
    flex-direction: column;
    align-items: center;
    gap: 2px;
  }
  .label-mark .name-row {
    display: flex;
    align-items: center;
    gap: 12px;
  }
  .label-mark .dot {
    width: 34px; height: 34px;
    border-radius: 50%;
    background: var(--mark-pink);
  }
  .label-mark .name {
    font-weight: 500;
    font-size: 38px;
    color: var(--ink);
    line-height: 1.1;
  }
  .label-mark .tagline {
    font-weight: 300;
    font-size: 18px;
    color: var(--mark-blue);
    padding-left: 46px;
  }
</style>
</head>
<body>
  <main class="album-cover">
    <div class="cover-frame"></div>
    <div class="soundwave-art" role="img" aria-label="Onde sonore symétrique remplie d’une nébuleuse étoilée, indigo aux bords et lumineuse au centre"></div>
    <div class="artist-title">
      <span class="rule"></span>
      <h1>KEMATRUVI</h1>
      <span class="rule"></span>
    </div>
    <div class="label-mark">
      <div class="name-row">
        <span class="dot"></span>
        <span class="name">KemaTruvi</span>
      </div>
      <span class="tagline">Cueillir la brume</span>
    </div>
  </main>
</body>
</html>
```